Flyer-Design für KFZ Onlineshop
Zielgruppe
Wir sind ein reiner Onlineshop, der sich auf Teile für das optische Auftreten von Fahrzeugen spezialisiert hat. Unsere vier verschiedenen Kategorien sind:
Fahrwerkstechnik, Aerodynamik (Anbauteile), Reinigungs- und Pflegemittel und Sonstiges (3D Kennzeichen, Kennzeichenhalterungen, Radbefestigungen, Gutscheine,..).
Aufgabenstellung
Der Flyer sollte das Format 10,5 x 21 cm (DIN lang) haben.
Die Kategorien sollten auf dem Flyer stehen, zusätzlich unsere Anschrift und unser vorhandenes Logo.
Schriftart: Einige Texte bitte in den Schriftarten 'Formation Sans Regular' und 'BankGothic Lt BT'.
Farben: C=0, M=0, Y=0, K=80 (Grau), C=100, M=20, Y=0, K=0 (Blau)

```html
<!DOCTYPE html>
<html lang="de">
<head>
<meta charset="utf-8">
<title>Flyer KFZ Onlineshop</title>
<link rel="stylesheet" href="https://fonts.googleapis.com/css2?family=Michroma&family=Syncopate&display=swap">
<style>
  :root {
    --backdrop: #c8c9cb;
    --paper: #ffffff;
    --grey-dark: #58595b;
    --grey-mid: #7b7c7e;
    --grey-light: #e9e9ea;
    --text-grey: #555658;
    --rule: #8a8a8c;
    --blue: #0093d9;
    --blue-light: #5cc6f3;
  }
  * { margin: 0; padding: 0; box-sizing: border-box; }
  html, body { width: 1200px; height: 2400px; overflow: hidden; }
  body { background: var(--backdrop); position: relative; font-family: "Syncopate", sans-serif; }
  .flyer {
    position: absolute; left: 96px; top: 208px; width: 998px; height: 1998px;
    background: var(--paper); overflow: hidden;
    box-shadow: 0 4px 14px rgba(0,0,0,0.25);
  }
  .flyer-shapes { position: absolute; inset: 0; width: 998px; height: 1998px; }
  .logo-name {
    position: absolute; top: 236px; left: 0; width: 100%; text-align: center;
    font-family: "Michroma", sans-serif; font-size: 62px; letter-spacing: 8px;
    color: var(--text-grey);
  }
  .headline {
    position: absolute; left: 104px; top: 532px;
    font-family: "Michroma", sans-serif; font-size: 82px; letter-spacing: 6px;
    color: var(--blue); line-height: 1;
  }
  .tagline {
    position: absolute; left: 110px; top: 636px; width: 800px;
    font-size: 40px; line-height: 80px; letter-spacing: 3px; color: var(--text-grey);
  }
  .divider {
    position: absolute; left: 110px; top: 887px; width: 762px; height: 2px; background: var(--rule);
  }
  .categories { position: absolute; left: 104px; top: 1000px; list-style: none; }
  .categories li {
    display: flex; align-items: center; height: 56px;
    font-size: 33px; letter-spacing: 3px; color: var(--text-grey);
  }
  .categories svg { width: 34px; height: 28px; margin-right: 34px; flex: none; }
  .subcategories { position: absolute; left: 326px; top: 1226px; list-style: none; }
  .subcategories li {
    height: 48px; line-height: 48px;
    font-size: 27px; letter-spacing: 3px; color: var(--text-grey);
  }
  .address {
    position: absolute; top: 1800px; left: 0; width: 100%; text-align: center;
    color: #fff; font-size: 30px; letter-spacing: 3px; line-height: 46px;
  }
  .address svg { width: 24px; height: 32px; display: block; margin: 0 auto 22px; }
</style>
</head>
<body>
  <div class="flyer">
    <svg class="flyer-shapes" viewBox="0 0 998 1998" aria-hidden="true">
      <path d="M0 0 H998 V244 Q850 70 500 92 Q200 110 0 224 Z" fill="var(--grey-dark)"/>
      <path d="M0 1592 Q420 1540 998 1610 V1998 H0 Z" fill="var(--grey-light)"/>
      <path d="M0 1708 Q480 1640 998 1622 V1664 Q520 1690 0 1740 Z" fill="var(--blue)"/>
      <path d="M800 1700 Q900 1640 998 1620 V1780 Q900 1740 800 1700 Z" fill="var(--blue-light)"/>
      <path d="M0 1740 Q520 1690 998 1664 V1780 Q500 1740 0 1790 Z" fill="var(--grey-light)"/>
      <path d="M0 1718 Q500 1800 998 1800 V1998 H0 Z" fill="var(--grey-dark)"/>
      <path d="M180 1998 Q560 1830 998 1800 V1998 Z" fill="var(--grey-mid)"/>
    </svg>

    <div class="logo-name">YOUR LOGO</div>

    <h1 class="headline">ONLINESHOP</h1>
    <p class="tagline">sich auf Teile für das optische</p>
    <div class="divider"></div>

    <ul class="categories">
      <li><svg viewBox="0 0 34 28"><path d="M3 3 L13 14 L3 25 M17 3 L27 14 L17 25" fill="none" stroke="var(--blue)" stroke-width="4"/></svg>Fahrwerkstechnik</li>
      <li><svg viewBox="0 0 34 28"><path d="M3 3 L13 14 L3 25 M17 3 L27 14 L17 25" fill="none" stroke="var(--blue)" stroke-width="4"/></svg>Aerodynamik (Anbauteile)</li>
      <li><svg viewBox="0 0 34 28"><path d="M3 3 L13 14 L3 25 M17 3 L27 14 L17 25" fill="none" stroke="var(--blue)" stroke-width="4"/></svg>Reinigungs- und Pflegemittel</li>
      <li><svg viewBox="0 0 34 28"><path d="M3 3 L13 14 L3 25 M17 3 L27 14 L17 25" fill="none" stroke="var(--blue)" stroke-width="4"/></svg>Sonstiges</li>
    </ul>

    <ul class="subcategories">
      <li>- 3D Kennzeichen</li>
      <li>- Kennzeichenhalterungen</li>
      <li>- Radbefestigungen</li>
      <li>- Gutscheine</li>
      <li>- ..............</li>
    </ul>

    <address class="address" style="font-style: normal;">
      <svg viewBox="0 0 24 32"><path d="M12 0 C5 0 0 5 0 12 C0 20 12 32 12 32 C12 32 24 20 24 12 C24 5 19 0 12 0 Z M12 7 A5 5 0 1 1 11.9 7 Z" fill="#fff" fill-rule="evenodd"/></svg>
      Lindenweg 27,<br>80997 München
    </address>
  </div>
</body>
</html>
```